need a Flyer for Plush Toy company

Need a Flyer for Plush Toy company ,

I upload a file for TEXT

Target Market(s)

Toys wholesalers , Supermarket

Industry/Entity Type

Toy Store

Colors
000000
ec1f27
c4c4c4

Requirements
Must have
• I have up loaded 3 files
• 1. Logo Registered Brand
• 2. customer's design in drawing
• 3. our ready samples based on Design
Nice to have
• happy kids in Nature ,
• happy kids in Ski ,
• different color Kids ,
• Multi culture concept

```html
<!DOCTYPE html>
<html lang="en">
<head>
<meta charset="utf-8">
<title>Mira Sole – Plush Toy Flyer</title>
<link rel="stylesheet" href="https://fonts.googleapis.com/css2?family=Play:wght@700&family=Source+Sans+3:wght@400;600&family=Gochi+Hand&display=swap">
<style>
  :root{
    --red:#ec1f27;
    --red-dark:#c8161d;
    --grey:#c4c4c4;
    --grey-light:#f1f1f1;
    --ink:#1a1a1a;
    --white:#ffffff;
  }
  *{box-sizing:border-box;margin:0;padding:0}
  html,body{width:913px;height:1200px;overflow:hidden;background:#e6e6e6}
  .flyer{position:relative;width:913px;height:1200px;background:var(--grey-light);overflow:hidden;font-family:"Source Sans 3",sans-serif;color:var(--ink)}
  .backdrop{position:absolute;inset:0}
  .brand{position:absolute;left:70px;top:100px;display:flex;align-items:center;gap:12px}
  .brand-dot{width:26px;height:26px;border-radius:50%;background:var(--red)}
  .brand-name{font-family:"Play",sans-serif;font-weight:700;font-size:40px;color:var(--red)}
  .tagline{position:absolute;left:22px;top:248px;font-family:"Gochi Hand",cursive;font-size:42px;color:var(--red)}
  .intro-heading{position:absolute;left:0;width:495px;top:455px;text-align:center;font-family:"Play",sans-serif;font-weight:700;color:var(--red-dark);font-size:23px;line-height:31.5px;letter-spacing:.6px}
  .intro-copy{position:absolute;left:22px;top:617px;width:474px;font-size:19px;line-height:24.5px;text-align:justify;letter-spacing:-.3px}
  .intro-copy p+p{margin-top:24px}
  .offer{position:absolute;left:520px;top:413px;width:371px;height:597px;background:var(--red);border-radius:0 0 16px 16px;color:var(--white);padding:0 30px 0 30px}
  .offer-photo{position:absolute;left:0;top:66px;width:371px;height:128px}
  .offer-title{position:absolute;left:34px;top:218px;font-family:"Play",sans-serif;font-weight:700;font-size:35px;letter-spacing:1px}
  .offer-body{position:absolute;left:30px;top:280px;width:313px;font-size:18.5px;line-height:22.5px;text-align:justify;letter-spacing:-.3px}
  .offer-body p+p{margin-top:20px}
  .offer-rule{position:absolute;left:30px;top:507px;width:313px;height:2px;background:rgba(255,255,255,.7)}
  .bank{position:absolute;left:30px;top:522px;font-size:13.5px;line-height:19.5px;letter-spacing:-.2px}
  .bank strong{font-weight:600}
  .footer-address{position:absolute;left:22px;top:1158px;font-size:19px;color:var(--white)}
  .footer-contact{position:absolute;right:54px;top:1098px;text-align:right;font-size:14.5px;line-height:19.5px;color:var(--white);letter-spacing:.3px}
</style>
</head>
<body>
<main class="flyer">
  <svg class="backdrop" width="913" height="1200" viewBox="0 0 913 1200" aria-hidden="false">
    <defs>
      <linearGradient id="kidsTone" x1="0" y1="0" x2="1" y2="1">
        <stop offset="0" stop-color="#6fa0d8"/>
        <stop offset=".45" stop-color="#d9a385"/>
        <stop offset=".8" stop-color="#f0c43a"/>
        <stop offset="1" stop-color="#5c8a3d"/>
      </linearGradient>
      <radialGradient id="babyTone" cx=".5" cy=".45" r=".6">
        <stop offset="0" stop-color="#f3e4d6"/>
        <stop offset=".7" stop-color="#e9d8c8"/>
        <stop offset="1" stop-color="#c9b8a8"/>
      </radialGradient>
      <linearGradient id="sofaTone" x1="0" y1="0" x2="1" y2="0">
        <stop offset="0" stop-color="#f3d6dc"/>
        <stop offset=".5" stop-color="#b9d9b4"/>
        <stop offset="1" stop-color="#f2e27a"/>
      </linearGradient>
    </defs>
    <!-- white upper area -->
    <path d="M0 0H913V300H0Z" fill="var(--white)"/>
    <path d="M0 0H560V330C440 320 200 320 0 318Z" fill="var(--white)"/>
    <!-- grey and red sweep -->
    <path d="M0 315C140 320 280 330 380 340L380 360C280 350 140 350 0 362Z" fill="var(--grey)"/>
    <path d="M0 362C140 350 280 350 380 360C250 364 110 380 0 420Z" fill="var(--red)"/>
    <path d="M0 420C110 380 250 364 380 360L380 400H0Z" fill="var(--grey-light)"/>
    <!-- kids photo ring -->
    <circle cx="671" cy="195" r="262" fill="var(--red)"/>
    <circle cx="676" cy="190" r="250" fill="var(--grey)"/>
    <circle cx="680" cy="186" r="240" fill="var(--white)"/>
    <circle cx="682" cy="180" r="232" fill="url(#kidsTone)" role="img" aria-label="Photo: a circle of smiling children from different cultures lying on grass"/>
    <!-- baby photo -->
    <circle cx="479" cy="368" r="112" fill="var(--grey)"/>
    <circle cx="479" cy="368" r="105" fill="var(--white)"/>
    <circle cx="479" cy="368" r="100" fill="url(#babyTone)" role="img" aria-label="Photo: laughing baby holding a yellow plush chick"/>
    <!-- sofa illustration placeholder -->
    <rect x="28" y="838" width="444" height="164" rx="14" fill="url(#sofaTone)" role="img" aria-label="Illustration: plush animal characters sitting on a green sofa"/>
    <!-- bottom waves -->
    <path d="M0 1035C150 1110 300 1120 520 1075C680 1040 800 1025 913 1020V1200H0Z" fill="var(--grey)"/>
    <path d="M0 1060C150 1125 320 1130 520 1090C690 1055 810 1045 913 1042V1200H0Z" fill="var(--white)"/>
    <path d="M0 1085C150 1140 330 1145 520 1105C700 1068 820 1062 913 1060V1200H0Z" fill="var(--red)"/>
  </svg>

  <div class="brand">
    <span class="brand-dot"></span>
    <span class="brand-name">Kaperkind</span>
  </div>
  <p class="tagline">Have you been there?</p>

  <h1 class="intro-heading">
    MIRA SOLE,<br>
    einzelunternehmen / Family business<br>
    Innovative Developer for Plush Toys<br>
    International Trader for Toys
  </h1>

  <div class="intro-copy">
    <p>We live and work in Bergheim near to Cologne Germany. We speak German and English.</p>
    <p>The toys are made in China, we are small family business, but we are professional in Plush toys business, right now we have successfully launched Projects with a huge Japanese 100 Yen Chain Store.</p>
  </div>

  <section class="offer">
    <svg class="offer-photo" viewBox="0 0 371 128" role="img" aria-label="Photo: row of colourful plush toy samples">
      <defs>
        <linearGradient id="plushTone" x1="0" y1="0" x2="1" y2="0">
          <stop offset="0" stop-color="#f6c6d4"/>
          <stop offset=".35" stop-color="#f4f1ea"/>
          <stop offset=".6" stop-color="#b8a6d6"/>
          <stop offset=".8" stop-color="#8fc6de"/>
          <stop offset="1" stop-color="#f5d63c"/>
        </linearGradient>
      </defs>
      <rect x="4" y="6" width="363" height="116" rx="40" fill="url(#plushTone)"/>
    </svg>
    <h2 class="offer-title">PLUSH TOY</h2>
    <div class="offer-body">
      <p>100 Yen = 0.90 USD</p>
      <p>Our products can meet strictest Quality Control, but are with extremely Low Price to fit for Japanese Dollar Shop as well as his overseas Store around the world.</p>
      <p>Of course our products are fit for Premium Store too.</p>
    </div>
    <div class="offer-rule"></div>
    <div class="bank">
      <strong>Bank information:</strong><br>
      Kontoinhaber/Account Holder: Lena Hoff<br>
      IBAN: DE12 3456 7890 1234 5678 00<br>
      BIC : EXMPDEFF100
    </div>
  </section>

  <p class="footer-address">Amselstraße 21, 50127 Bergheim Germany</p>
  <div class="footer-contact">
    hello@plushwerk.de<br>
    Fon &nbsp; +49 (0) 2271- 555 0101<br>
    Fax &nbsp; +49 (0) 2271- 555 0102<br>
    Mobil: &nbsp;+49 (0) 170 5550 103<br>
    Ust-IdNr./VAT No. DE000111222
  </div>
</main>
</body>
</html>
```